Leading car website needs banner ads + EDM

We are looking for a freelance graphic/web designer to create a set of 5 web banners and an EDM design, with associated HTML markup, to promote a competition for our leading car reviews website (http://www.motorvista.example). We are trying to promote a competition which encourages users to enter their own car reviews (i.e via: http://www.motorvista.example/reader-reviews/), with $1000 and $100 fuel vouchers (Veltrop Gaspoint) as the incentive.
We are essentially looking for one banner ad in 5 different sizes:
640x320 (static)
600x300 (static)
300x90 (animated)
300x250 (animated)
728x90 (animated)
+ an EDM newsletter which can be sent out to our database of users.
Ideally 3 of the ads will be made as animated gifs, with three frames of text that rotates. The text will be to the effect of:
1. "REVIEW YOUR CAR ON MOTORVISTA TO WIN!"
2. "WIN $1,000 PETROL"
3. "$1,000 FUEL EVERY MONTH +$100 FUEL EVERY WEEK"
*NOTE: All banners should also include "*Terms and conditions apply" in small, but visible, print somewhere on 1 frame
Designs among all banners and the EDM should use a consistant colour scheme and styling. All designs should include the motor vista logo as attached (on black OR white background) and an image of the Veltrop Gaspoint cards (the prize), as attached.
EDM: Should be 600 pixels wide and as deep as necessary to include the required header, copy and footer. The body background of the EDM should be white, in keeping with the website, using the logo on white background. The body should comprise of a header banner which is in the same style as the 640x320 (mentioned above), but only 600x300 in size. The main body copy is attached to this project in a word doc. The EDM should include a footer in similar styling as the footer used on the website (http://www.motorvista.example). There should be a graphical link to the website with the title "Add a User Review" and also a text link to "Terms and Conditions".
The EDM should be supplied in html format, along with all associated images.
Requirements
Must have
- - Must use motorvista logo
- Strong call to action
- All banners should also include "*Terms and conditions apply" in small, but visible, print somewhere on 1 frame
- Gaspoint image
Should not have
- - Strobe or flashing animation

```html
<!DOCTYPE html>
<html lang="en">
<head>
<meta charset="utf-8">
<title>Fuel Competition Leaderboard Banner</title>
<link rel="stylesheet" href="https://fonts.googleapis.com/css2?family=Anton&family=Arimo&display=swap">
<style>
  :root {
    --banner-bg: #000000;
    --fuel-orange-light: #ffb347;
    --fuel-orange: #f08a1c;
    --fuel-orange-deep: #c85f00;
    --headline-edge: #3a1a00;
    --fineprint: #ffffff;
  }
  html, body {
    margin: 0;
    padding: 0;
    width: 1200px;
    height: 148px;
    overflow: hidden;
    background: var(--banner-bg);
  }
  .banner {
    position: relative;
    width: 1200px;
    height: 148px;
    background: var(--banner-bg);
    overflow: hidden;
  }
  .banner__headline {
    position: absolute;
    left: 0;
    top: 0;
    width: 1200px;
    height: 148px;
  }
  .banner__headline-text {
    font-family: "Anton", "Impact", sans-serif;
    font-size: 64px;
    letter-spacing: 0;
  }
  .banner__fineprint {
    position: absolute;
    right: 35px;
    top: 110px;
    margin: 0;
    font-family: "Arimo", "Arial", sans-serif;
    font-size: 18px;
    color: var(--fineprint);
    white-space: nowrap;
  }
</style>
</head>
<body>
  <div class="banner">
    <svg class="banner__headline" viewBox="0 0 1200 148" aria-labelledby="headline-title">
      <title id="headline-title">$1,000 fuel every month + $100 fuel every week</title>
      <defs>
        <linearGradient id="fuel-fill" x1="0" y1="0" x2="0" y2="1">
          <stop offset="0" style="stop-color: var(--fuel-orange-light)"/>
          <stop offset="0.55" style="stop-color: var(--fuel-orange)"/>
          <stop offset="1" style="stop-color: var(--fuel-orange-deep)"/>
        </linearGradient>
      </defs>
      <text class="banner__headline-text" x="35" y="96" textLength="1128" lengthAdjust="spacingAndGlyphs"
            fill="var(--fuel-orange-deep)" transform="translate(2 2)">$1,000 FUEL EVERY MONTH+$100 FUEL EVERY WEEK</text>
      <text class="banner__headline-text" x="35" y="96" textLength="1128" lengthAdjust="spacingAndGlyphs"
            fill="url(#fuel-fill)" stroke="var(--headline-edge)" stroke-width="1.5" paint-order="stroke">$1,000 FUEL EVERY MONTH+$100 FUEL EVERY WEEK</text>
    </svg>
    <p class="banner__fineprint">Terms and conditions apply</p>
  </div>
</body>
</html>
```